Website incl. html for real estate project

We need the design and implementation of a website for a real estate project. Condominiums are built, which are sold.
We upload the sales brochure. The website should be based on the design of the sales brochure.
There are three houses with 5 apartments each. It should be rendered like this. The structure of the menu should be roughly as follows. Most information about the content is either in the appendix as a picture or in the brochure (PDF)):
Home (page 4-5 from the brochure)
House A
house B
house c
overview
basement
Municipal elections (page 6-7 in the brochure pdf)
Contact
Please use Roboto Regular as font.
And one page should give an overview of all apartments with the prices, the living space, etc. as on the file overview2.jpg.
If you go to the House A, House B, or House C menus, a page should come up with the details for that house only. The pages in the brochure are:
House A (Page 10-11)
House B (page 22-23)
House C (page 34-35)
The individual apartments should each be shown on a property page. There the plan / floor plan of the apartment and the pictures from the inside should be shown. As with the object page.jpg attachment.
Für die Designer... Mehr Zeit...
Coded - Design and coding required
1 page

```html
<!DOCTYPE html>
<html lang="de">
<head>
<meta charset="utf-8">
<title>Haus A – Haus Single Page</title>
<link href="https://fonts.googleapis.com/css2?family=Nunito+Sans:wght@400&family=Roboto:wght@300;400;500&display=swap" rel="stylesheet">
<style>
  :root {
    --board: #ebebeb;
    --page: #ffffff;
    --band: #f3f3f3;
    --ink: #111111;
    --text: #2b2b2b;
    --muted: #555555;
    --line: #d6d6d6;
    --accent: #5e5959;
    --field: #9a9a9a;
  }
  * { box-sizing: border-box; margin: 0; padding: 0; }
  html, body { width: 1200px; height: 3054px; overflow: hidden; }
  body { background: var(--board); font-family: "Roboto", sans-serif; color: var(--text); position: relative; }
  .abs { position: absolute; }

  .board-title { left: 0; width: 1200px; top: 124px; text-align: center; font-family: "Nunito Sans", sans-serif; font-size: 66px; font-weight: 400; color: #333; letter-spacing: 0.5px; }

  .page { left: 57px; top: 258px; width: 1086px; height: 2669px; background: var(--page); }

  .sidebar { left: 0; top: 0; width: 116px; height: 584px; border-right: 1px solid var(--line); }
  .brand { left: 58px; top: 395px; transform: translate(-50%, -50%) rotate(-90deg); font-size: 19px; font-weight: 400; letter-spacing: 3px; color: var(--ink); white-space: nowrap; }
  .side-contact { left: 58px; top: 378px; transform: translate(-50%, -50%) rotate(-90deg); font-size: 7.5px; line-height: 10px; color: var(--ink); white-space: nowrap; text-align: left; }
  .menu-btn { left: 32px; top: 493px; width: 52px; height: 52px; border-radius: 50%; border: 1px solid var(--line); display: flex; align-items: center; justify-content: center; }

  .hero { left: 116px; top: 0; width: 970px; height: 439px; background: linear-gradient(180deg, #a9b3a6 0%, #b8b3a8 35%, #9d978d 70%, #6f6b62 100%); }

  .house-title { left: 116px; width: 970px; top: 462px; text-align: center; font-size: 50px; font-weight: 500; color: var(--ink); }
  .house-intro { left: 190px; width: 780px; top: 548px; text-align: center; font-size: 15.5px; line-height: 27.5px; color: var(--ink); }

  .features { left: 116px; top: 718px; width: 970px; height: 405px; background: var(--band); }
  .feature { top: 53px; width: 205px; }
  .feature .pic { width: 205px; height: 137px; }
  .feature h3 { margin-top: 16px; font-size: 15.5px; font-weight: 400; color: var(--ink); }
  .feature p { margin-top: 10px; font-size: 10.5px; line-height: 16.6px; color: var(--muted); }

  .units-title { left: 116px; width: 970px; top: 1212px; text-align: center; font-size: 30px; font-weight: 400; color: var(--ink); }
  .unit { left: 151px; width: 750px; height: 113px; }
  .unit .thumb { left: 0; top: 0; width: 168px; height: 113px; }
  .unit .name { left: 198px; top: 28px; font-size: 16px; line-height: 22px; color: var(--ink); }
  .unit .area { font-size: 12.5px; color: var(--muted); margin-top: 4px; display: block; }
  .unit .stat { top: 32px; font-size: 12.5px; color: var(--muted); }
  .unit .go { left: 717px; top: 24px; width: 39px; height: 39px; border-radius: 50%; background: var(--accent); display: flex; align-items: center; justify-content: center; }
  .divider { left: 153px; width: 748px; height: 1px; background: var(--line); }

  .contact { left: 116px; top: 2126px; width: 970px; height: 543px; background: var(--band); text-align: center; }
  .contact h2 { position: absolute; left: 0; width: 970px; top: 50px; font-size: 28px; font-weight: 400; color: var(--ink); }
  .field { top: 106px; width: 292px; height: 40px; border: 1px solid var(--field); background: var(--page); font-size: 12px; color: #666; text-align: left; padding: 12px 26px; }
  .consent { left: 0; width: 970px; top: 185px; font-size: 10.5px; color: #333; display: flex; justify-content: center; align-items: center; gap: 6px; }
  .consent .box { width: 10px; height: 10px; background: #d5d5d5; }
  .send { left: 400px; top: 229px; width: 111px; height: 32px; border-radius: 16px; background: var(--accent); color: #fff; font-size: 12px; line-height: 32px; }
  .contact-lines { left: 0; width: 970px; top: 312px; color: var(--ink); }
  .contact-lines .big { font-size: 28px; line-height: 32px; font-weight: 300; }
  .contact-lines .addr { font-size: 15.5px; line-height: 22px; margin-top: 12px; }
  .social { top: 466px; display: flex; align-items: center; gap: 5px; font-size: 11px; color: var(--ink); }
  .social .dot { width: 16px; height: 16px; border-radius: 50%; background: var(--ink); }
</style>
</head>
<body>
  <h1 class="abs board-title">Haus Single Page</h1>

  <div class="abs page">
    <aside class="abs sidebar">
      <div class="abs brand">HALDENHOF</div>
      <div class="abs side-contact" style="top:647px;">+41 61 555 01 23<br>kontakt@haldenhof-wohnen.ch</div>
      <div class="abs menu-btn">
        <svg width="14" height="18" viewBox="0 0 14 18"><g stroke="#aaa" stroke-width="1"><line x1="3" y1="0" x2="3" y2="18"/><line x1="7" y1="0" x2="7" y2="18"/><line x1="11" y1="0" x2="11" y2="18"/></g></svg>
      </div>
    </aside>

    <div class="abs hero" role="img" aria-label="Aussenansicht von Haus A mit Balkonen und Gartensitzplatz"></div>

    <h2 class="abs house-title">Haus A</h2>
    <p class="abs house-intro">Das Gebäude «Haus A» verfügt über fünf moderne Wohnungen mit individuellen Grundrissen. Alle Wohnungen haben einen grosszügigen Aussenbereich mit Balkon oder gedecktem Sitzplatz in Richtung Süden zum Stürmenkopf, dem Wahlner Hausberg. Die Wohnräume sind mit grossen Fenstern ausgestattet, was die Räume mit Sonnenlicht durchflutet. Das Gebäude ist direkt aus der Tiefgarage mit dem Lift zugänglich.</p>

    <section class="abs features">
      <div class="abs feature" style="left:121px;">
        <div class="pic" role="img" aria-label="Luftbild der Gartenwohnungen und Balkone" style="background:linear-gradient(160deg,#d8d2c8,#b9ae9e 55%,#7f9a5c);"></div>
        <h3>Garten und Balkone</h3>
        <p>Die Gartenwohnungen verfügen über einen gedeckten Sitzplatz und eine ansprechende Gartenfläche und die Wohnungen im ersten Stock über einen sehr grosszügigen Balkon. Die Attikawohnung verfügt über eine riesige Terrasse, ein richtiger Wohntraum.</p>
      </div>
      <div class="abs feature" style="left:372px; top:57px;">
        <div class="pic" role="img" aria-label="Möblierter Grundriss einer Wohnung" style="background:linear-gradient(135deg,#e4e4e4,#c9c7c3 60%,#b7b3ad);"></div>
        <h3>Grundrisse</h3>
        <p>Die Aufteilung der Räume ist sehr effizient gestaltet. Der verfügbare Platz ist optimal genutzt. Jede Wohnung verfügt über ein praktisches Reduit</p>
      </div>
      <div class="abs feature" style="left:625px; top:61px;">
        <div class="pic" role="img" aria-label="Luftbild des Dorfes mit Hügeln im Hintergrund" style="background:linear-gradient(180deg,#8d9aa0,#53663e 40%,#6b7a4c 70%,#4d6233);"></div>
        <h3>Ausrichtung / Lage</h3>
        <p>Die Balkone, Sitzplätze und Wohnräume sind gegen Süd-Südwest ausgerichtet. Das verspricht eine Durchflutung der hellen Wohnräume mit Sonnenlicht.</p>
      </div>
    </section>

    <h2 class="abs units-title">Haus A Wohnungen</h2>

    <div class="abs unit" style="top:1290px; left:153px;">
      <div class="abs thumb" role="img" aria-label="Innenansicht Küche und Essbereich" style="background:linear-gradient(135deg,#e9e7e3,#cfcac2 60%,#b5aca0);"></div>
      <div class="abs name">Attika Wohnung Haus A<span class="area">102 m² Wohnfläche</span></div>
      <div class="abs stat" style="left:426px;">3 Schlafzimmer</div>
      <div class="abs stat" style="left:552px;">2 Badezimmer</div>
      <div class="abs go" style="left:715px;"><svg width="12" height="14" viewBox="0 0 12 14"><polyline points="4,2 9,7 4,12" fill="none" stroke="#fff" stroke-width="1.3"/></svg></div>
    </div>
    <div class="abs divider" style="top:1427px;"></div>

    <div class="abs unit" style="top:1444px;">
      <div class="abs thumb" role="img" aria-label="Innenansicht Wohnzimmer mit Sofa" style="background:linear-gradient(135deg,#ecebe8,#d3cfc8 55%,#8a7064);"></div>
      <div class="abs name">4,5Zimmer Wohnung<br>Obergeschoss, Haus A<span class="area" style="margin-top:0;">102 m² Wohnfläche</span></div>
      <div class="abs stat" style="left:426px;">2 Schlafzimmer</div>
      <div class="abs stat" style="left:552px;">2 Badezimmer</div>
      <div class="abs go"><svg width="12" height="14" viewBox="0 0 12 14"><polyline points="4,2 9,7 4,12" fill="none" stroke="#fff" stroke-width="1.3"/></svg></div>
    </div>
    <div class="abs divider" style="top:1574px;"></div>

    <div class="abs unit" style="top:1579px;">
      <div class="abs thumb" role="img" aria-label="Innenansicht Küche mit Esstisch" style="background:linear-gradient(135deg,#e8e6e2,#cbc5bb 60%,#a89a89);"></div>
      <div class="abs name">3 1/5 Zimmer Wohnung<br>Erdgeschoss, Haus A<span class="area">102 m² Wohnfläche</span></div>
      <div class="abs stat" style="left:426px;">3 Schlafzimmer</div>
      <div class="abs stat" style="left:552px;">2 Badezimmer</div>
      <div class="abs go"><svg width="12" height="14" viewBox="0 0 12 14"><polyline points="4,2 9,7 4,12" fill="none" stroke="#fff" stroke-width="1.3"/></svg></div>
    </div>
    <div class="abs divider" style="top:1702px;"></div>

    <div class="abs unit" style="top:1719px; left:149px;">
      <div class="abs thumb" role="img" aria-label="Innenansicht Küche und Essbereich" style="background:linear-gradient(135deg,#e9e7e3,#cfcac2 60%,#b5aca0);"></div>
      <div class="abs name">4,5Zimmer Wohnung<br>Obergeschoss, Haus A<span class="area" style="margin-top:0;">102 m² Wohnfläche</span></div>
      <div class="abs stat" style="left:426px;">2 Schlafzimmer</div>
      <div class="abs stat" style="left:552px;">2 Badezimmer</div>
      <div class="abs go" style="left:719px;"><svg width="12" height="14" viewBox="0 0 12 14"><polyline points="4,2 9,7 4,12" fill="none" stroke="#fff" stroke-width="1.3"/></svg></div>
    </div>
    <div class="abs divider" style="top:1849px; left:151px;"></div>

    <div class="abs unit" style="top:1866px;">
      <div class="abs thumb" role="img" aria-label="Innenansicht Wohnzimmer mit Sofa" style="background:linear-gradient(135deg,#ecebe8,#d3cfc8 55%,#8a7064);"></div>
      <div class="abs name">4,5 Zimmer Wohnung<br>Erdgeschoss, Haus A<span class="area">102 m² Wohnfläche</span></div>
      <div class="abs stat" style="left:426px;">3 Schlafzimmer</div>
      <div class="abs stat" style="left:552px;">2 Badezimmer</div>
      <div class="abs go"><svg width="12" height="14" viewBox="0 0 12 14"><polyline points="4,2 9,7 4,12" fill="none" stroke="#fff" stroke-width="1.3"/></svg></div>
    </div>

    <section class="abs contact">
      <h2>Kontakt</h2>
      <div class="abs field" style="left:160px;">Name*</div>
      <div class="abs field" style="left:477px;">Email*</div>
      <div class="abs consent"><span class="box"></span>I accept The Terms for processing personal data.</div>
      <div class="abs send">Send Request</div>
      <div class="abs contact-lines">
        <div class="big">+41 61 555 01 23</div>
        <div class="big">kontakt@haldenhof-wohnen.ch</div>
        <div class="addr">Mara Keller, 12 Linden Road,<br>Elmwood, Vermont 05400</div>
      </div>
      <div class="abs social" style="left:386px;"><span class="dot"></span>Teilen</div>
      <div class="abs social" style="left:506px;"><span class="dot"></span>Netz</div>
    </section>
  </div>
</body>
</html>
```